A start-up named "Corvath Therapeutics" - needs a new PowerPoint design

We need a new PowerPoint Design for an early-stage start-up named "Corvath Therapeutics" seeking to disrupt the current approach towards drug discovery within aging disorders.

We would like to build on Corvath's legacy, the founder of the modern science of genetics, by employing a multidisciplinary approach, experimenting, and providing elderly patients the attention they deserve.

We have selected the suffix "therapeutics" intentionally as it stands for (a medicine) the treatment of disease; the science of healing. Alzheimer’s treatment is a huge, urgent, unmet need:
- Shift from a disease-management system to a preventive medicine system
- Focus on increasing the health span, not only the life span

Target Market(s)

Pharma/ Biotech Executives Medical Institutions Healthcare professionals (MDs, nurses, payors, pharmacists, etc.) Patients

Industry/Entity Type

Healthcare

Other font styles liked:
• Celias

Colors
0054AA
0677BA
7BADD7
CADEEF
E8F1F8
E54698
E96AAD
F1A4CE
F9D9EA
FCEFF6
A7469A
B969AE
D3A5CF
EDDBEB
F8F0F9
6B429C
8869AF
B7A5CE
E3DAEB
F3F0F8

Requirements
Must have
• - differentiate from other companies named after Corvath - differentiate from other Pharma/ Biotech companies
Nice to have
• simplicity/ minimalist logo vivid colors gradient 3D Life-Sciences inspired Simple geometry Balance
Should not have
• mascot/ emblem watermark logo animated ink style nature-inspired inventive typography artistic chaos

```html
<!DOCTYPE html>
<html lang="en">
<head>
<meta charset="utf-8">
<title>Corvath Therapeutics – Presentation Template</title>
<link href="https://fonts.googleapis.com/css2?family=Outfit:wght@300;400;500;600&display=swap" rel="stylesheet">
<style>
  :root{
    --canvas:#ececec;
    --white:#ffffff;
    --ink:#161616;
    --muted:#7a7a7a;
    --cyan:#2bb3e3;
    --blue:#0677ba;
    --violet:#6b429c;
    --purple:#8a2a94;
    --lilac:#b969ae;
    --photo-warm:#b8a79a;
    --photo-cool:#8a9fae;
  }
  *{box-sizing:border-box;margin:0;padding:0}
  html,body{width:1200px;height:908px;overflow:hidden}
  body{background:var(--canvas);font-family:"Outfit",sans-serif;color:var(--ink);position:relative}
  .defs{position:absolute;width:0;height:0}
  .slide{position:absolute;width:267px;height:150px;background:var(--white);box-shadow:0 1px 3px rgba(0,0,0,.22);overflow:hidden}
  .slide svg.art{position:absolute;left:0;top:0;width:267px;height:150px}
  .abs{position:absolute}
  .title{font-size:11px;font-weight:500;line-height:1;letter-spacing:-.1px}
  .title-center{position:absolute;left:0;right:0;text-align:center;font-size:10.5px;font-weight:500}
  .rule{position:absolute;width:14px;height:1px;background:linear-gradient(90deg,var(--cyan),var(--violet))}
  .body{font-size:2.7px;line-height:1.55;color:var(--muted)}
  .label{font-size:2.9px;font-weight:600;letter-spacing:.35px;text-transform:uppercase;color:var(--ink)}
  .quote{font-size:6.6px;font-weight:500;line-height:1.15;text-align:center}
  .photo{position:absolute}
  .wordmark{position:absolute;text-align:left;font-weight:500;line-height:1}
  .wordmark b{display:block;font-weight:500}
  .wordmark span{display:block;font-weight:500;letter-spacing:.9px}
</style>
</head>
<body>

<svg class="defs" aria-hidden="true">
  <defs>
    <linearGradient id="line-grad" x1="0" y1="0" x2="1" y2="1">
      <stop offset="0" stop-color="#2bb3e3"/>
      <stop offset="1" stop-color="#7a2d98"/>
    </linearGradient>
    <linearGradient id="photo-warm" x1="0" y1="0" x2="1" y2="1">
      <stop offset="0" stop-color="#d8cfc7"/>
      <stop offset=".5" stop-color="#9a8b82"/>
      <stop offset="1" stop-color="#5c5660"/>
    </linearGradient>
    <linearGradient id="photo-cool" x1="0" y1="0" x2="1" y2="1">
      <stop offset="0" stop-color="#b8c4cc"/>
      <stop offset="1" stop-color="#4c5a6a"/>
    </linearGradient>
  </defs>
</svg>

<!-- Row 1 -->
<section class="slide cover" style="left:36px;top:37px;background:linear-gradient(90deg,#2bb3e3 0%,#6a5bb0 45%,#8a2a94 100%)">
  <div class="wordmark" style="left:96px;top:61px;color:#fff">
    <b style="font-size:15px">Corvath</b>
    <span style="font-size:6.4px;margin-top:1px">Therapeutics</span>
  </div>
</section>

<section class="slide quote-slide" style="left:324px;top:37px">
  <svg class="art" viewBox="0 0 267 150">
    <path role="img" aria-label="Photo of a businessman seated by a window" d="M35 0 L230 0 C232 40 175 92 102 103 C62 110 30 92 33 50 Z" fill="url(#photo-cool)" stroke="#7a3a9c" stroke-width=".8"/>
  </svg>
  <p class="abs quote" style="left:138px;top:106px;width:86px">”Here you can write an inspirational quote”</p>
</section>

<section class="slide problem" style="left:611px;top:37px">
  <svg class="art" viewBox="0 0 267 150">
    <path d="M267 1 Q190 30 204 74 Q212 128 267 150" fill="none" stroke="url(#line-grad)" stroke-width=".6"/>
    <g fill="#fff" stroke="url(#line-grad)" stroke-width=".8">
      <circle cx="214" cy="41" r="10"/><circle cx="204" cy="74" r="10"/><circle cx="214" cy="109" r="10"/>
    </g>
    <g fill="none" stroke="#6b429c" stroke-width=".6" stroke-linejoin="round">
      <rect x="210.5" y="40" width="7" height="5.5" rx=".6"/><path d="M212 40 v-2 a2 2 0 0 1 4 0 v2"/>
      <path d="M200 78 l1-3 6-6 2 2-6 6z"/>
      <path d="M210 105 h8 l-3 4 v4 l-2 -1 v-3z"/>
    </g>
  </svg>
  <h2 class="abs title" style="left:40px;top:50px">The<br>Problem</h2>
  <div class="rule" style="left:40px;top:77px"></div>
  <p class="abs body" style="left:40px;top:82px;width:58px">Mauris id interdum sapien, in convallis nulla. Integer laoreet nunc ut pharetra consequat. Cras sodales congue ante, eu blandit nulla hendrerit sed.</p>
  <div class="abs" style="left:128px;top:31px;width:72px;text-align:right">
    <p class="label">Problem 1</p><p class="body">Mauris id interdum sapien, in convallis nulla. Integer laoreet nunc ut pharetra.</p>
  </div>
  <div class="abs" style="left:118px;top:65px;width:72px;text-align:right">
    <p class="label">Problem 2</p><p class="body">Mauris id interdum sapien, in convallis nulla. Integer laoreet nunc ut pharetra.</p>
  </div>
  <div class="abs" style="left:128px;top:99px;width:72px;text-align:right">
    <p class="label">Problem 3</p><p class="body">Mauris id interdum sapien, in convallis nulla. Integer laoreet nunc ut pharetra.</p>
  </div>
</section>

<section class="slide vision" style="left:899px;top:37px">
  <svg class="art" viewBox="0 0 267 150">
    <g fill="#fff" stroke="url(#line-grad)" stroke-width=".8">
      <rect x="-18.5" y="-18.5" width="37" height="37" rx="8" transform="translate(168 42) rotate(45)"/>
      <rect x="-18.5" y="-18.5" width="37" height="37" rx="8" transform="translate(129 74) rotate(45)"/>
      <rect x="-18.5" y="-18.5" width="37" height="37" rx="8" transform="translate(208 74) rotate(45)"/>
      <rect x="-18.5" y="-18.5" width="37" height="37" rx="8" transform="translate(168 107) rotate(45)"/>
    </g>
    <g fill="none" stroke="#333" stroke-width=".5" stroke-linejoin="round">
      <path d="M165 32 l1-3 5-5 2 2-5 5z"/>
      <path d="M126 64 l1-3 5-5 2 2-5 5z"/>
      <rect x="205" y="62" width="6" height="5" rx=".5"/><path d="M206.3 62 v-1.6 a1.7 1.7 0 0 1 3.4 0 v1.6"/>
      <path d="M164 91 h8 l-3 4 v3 l-2 -1 v-2z"/>
    </g>
  </svg>
  <h2 class="abs title" style="left:40px;top:50px">Our<br>Vision</h2>
  <div class="rule" style="left:40px;top:77px"></div>
  <p class="abs body" style="left:40px;top:82px;width:58px">Mauris id interdum sapien, in convallis nulla. Integer laoreet nunc ut pharetra consequat. Cras sodales congue ante, eu blandit nulla hendrerit sed.</p>
  <div class="abs" style="left:148px;top:41px;width:40px;text-align:center"><p class="label">Bullet point</p><p class="body">Sample text here.<br>Two lines.</p></div>
  <div class="abs" style="left:109px;top:73px;width:40px;text-align:center"><p class="label">Bullet point</p><p class="body">Sample text here.<br>Two lines.</p></div>
  <div class="abs" style="left:188px;top:73px;width:40px;text-align:center"><p class="label">Bullet point</p><p class="body">Sample text here.<br>Two lines.</p></div>
  <div class="abs" style="left:148px;top:105px;width:40px;text-align:center"><p class="label">Bullet point</p><p class="body">Sample text here.<br>Two lines.</p></div>
</section>

<!-- Row 2 -->
<section class="slide mission" style="left:36px;top:208px">
  <div class="photo" role="img" aria-label="Photo of an elderly couple sitting together" style="left:0;top:0;width:74px;height:150px;background:linear-gradient(135deg,#d9d2cf,#a99488 55%,#6f6c78);border-right:.8px solid #7a3a9c"></div>
  <h2 class="abs title" style="left:84px;top:45px">Our<br>Mission</h2>
  <div class="rule" style="left:85px;top:74px"></div>
  <p class="abs body" style="left:81px;top:79px;width:58px">Mauris id interdum sapien, in convallis nulla. Integer laoreet nunc ut pharetra consequat. Cras sodales congue ante, eu blandit nulla hendrerit sed.</p>
  <div class="abs" style="left:166px;top:32px;width:62px">
    <p class="body" style="color:var(--ink);font-weight:600">Mission 1</p><p class="body" style="margin-bottom:11px">Vestibulum imperdiet pharetra nibh<br>at sodales.</p>
    <p class="body" style="color:var(--ink);font-weight:600">Mission 2</p><p class="body" style="margin-bottom:11px">Vestibulum imperdiet pharetra nibh<br>at sodales.</p>
    <p class="body" style="color:var(--ink);font-weight:600">Mission 3</p><p class="body" style="margin-bottom:11px">Vestibulum imperdiet pharetra nibh<br>at sodales.</p>
    <p class="body" style="color:var(--ink);font-weight:600">Mission 4</p><p class="body">Vestibulum imperdiet pharetra nibh<br>at sodales.</p>
  </div>
</section>

<section class="slide value" style="left:324px;top:208px">
  <svg class="art" viewBox="0 0 267 150">
    <path role="img" aria-label="Photo of a patient resting in bed with a visitor" d="M0 35 C15 18 40 10 58 17 C75 25 92 65 98 85 C102 105 88 113 65 116 C40 119 15 118 0 115 Z" fill="url(#photo-warm)" stroke="url(#line-grad)" stroke-width=".8"/>
  </svg>
  <h2 class="abs title" style="left:109px;top:37px">Value Proposition</h2>
  <p class="abs body" style="left:109px;top:54px;width:106px">Suspendisse ultricies velit velit, et blandit nibh feugiat sed. Donec a nisl elit. Aenean dictum odio sit amet dictum luctus. Proin molestie odio purus, vel laoreet odio convallis vel. Class aptent taciti sociosqu ad litora torquent.</p>
  <p class="abs body" style="left:109px;top:92px;width:106px">Suspendisse ultricies velit velit, et blandit nibh feugiat sed. Donec a nisl elit. Aenean dictum odio sit amet dictum luctus purus.</p>
</section>

<section class="slide quote-photo" style="left:611px;top:208px">
  <div class="photo" role="img" aria-label="Photo of two women embracing by a window, with a purple tint" style="inset:0;background:linear-gradient(90deg,#a9bccb 0%,#9a8fb4 40%,#9a5aa6 75%,#8a3a9a 100%)"></div>
  <p class="abs quote" style="left:22px;top:82px;width:96px;color:#fff;font-size:6.2px">”Here you can write another inspirational quote or company goal”</p>
</section>

<section class="slide team" style="left:899px;top:208px">
  <h2 class="title-center" style="top:25px">Meet our team</h2>
  <svg class="art" viewBox="0 0 267 150">
    <g stroke="url(#line-grad)" stroke-width=".8" stroke-linejoin="round">
      <polygon role="img" aria-label="Team member portrait" transform="translate(75 66)" points="0,-18 15.6,-9 15.6,9 0,18 -15.6,9 -15.6,-9" fill="url(#photo-warm)"/>
      <polygon role="img" aria-label="Team member portrait" transform="translate(133 66)" points="0,-18 15.6,-9 15.6,9 0,18 -15.6,9 -15.6,-9" fill="url(#photo-cool)"/>
      <polygon role="img" aria-label="Team member portrait" transform="translate(191 66)" points="0,-18 15.6,-9 15.6,9 0,18 -15.6,9 -15.6,-9" fill="url(#photo-warm)"/>
    </g>
    <g stroke="url(#line-grad)" stroke-width=".6">
      <line x1="70" y1="103" x2="80" y2="103"/><line x1="128" y1="103" x2="138" y2="103"/><line x1="186" y1="103" x2="196" y2="103"/>
    </g>
  </svg>
  <div class="abs" style="left:50px;top:89px;width:50px;text-align:center"><p class="label">Name 1</p><p class="body">Job position</p><p class="body" style="margin-top:6px">Mauris id interdum sapien, in convallis nulla. Integer laoreet nunc ut pharetra consequat.</p></div>
  <div class="abs" style="left:108px;top:89px;width:50px;text-align:center"><p class="label">Name 2</p><p class="body">Job position</p><p class="body" style="margin-top:6px">Mauris id interdum sapien, in convallis nulla. Integer laoreet nunc ut pharetra consequat.</p></div>
  <div class="abs" style="left:166px;top:89px;width:50px;text-align:center"><p class="label">Name 3</p><p class="body">Job position</p><p class="body" style="margin-top:6px">Mauris id interdum sapien, in convallis nulla. Integer laoreet nunc ut pharetra consequat.</p></div>
</section>

<!-- Row 3 -->
<section class="slide roadmap" style="left:36px;top:379px">
  <svg class="art" viewBox="0 0 267 150">
    <line x1="56" y1="50" x2="214" y2="50" stroke="url(#line-grad)" stroke-width=".6"/>
    <g fill="#fff" stroke="url(#line-grad)" stroke-width=".8">
      <rect x="-14" y="-14" width="28" height="28" rx="10" transform="translate(56 50) rotate(15)"/>
      <rect x="-13" y="-13" width="26" height="26" rx="10" transform="translate(111 50) rotate(-12)"/>
      <rect x="-13" y="-13" width="26" height="26" rx="10" transform="translate(163 50) rotate(20)"/>
      <rect x="-13" y="-13" width="26" height="26" rx="10" transform="translate(214 50) rotate(-18)"/>
    </g>
  </svg>
  <div class="abs body" style="left:44px;top:44px;width:24px;text-align:center;color:var(--ink);letter-spacing:.3px"><b>2019</b><br>Title and<br>text here</div>
  <div class="abs body" style="left:99px;top:44px;width:24px;text-align:center;color:var(--ink);letter-spacing:.3px"><b>2022</b><br>Title and<br>text here</div>
  <div class="abs body" style="left:151px;top:44px;width:24px;text-align:center;color:var(--ink);letter-spacing:.3px"><b>2026</b><br>Title and<br>text here</div>
  <div class="abs body" style="left:202px;top:44px;width:24px;text-align:center;color:var(--ink);letter-spacing:.3px"><b>2030</b><br>Title and<br>text here</div>
  <h2 class="abs title" style="left:50px;top:87px;width:54px;text-align:right;font-size:10px">Company Roadmap</h2>
  <div class="rule" style="left:88px;top:114px"></div>
  <p class="abs body" style="left:114px;top:87px;width:114px;color:#444">Lorem ipsum dolor sit amet, consectetur adipiscing elit. Morbi convallis mi leo, id pharetra urna scelerisque sit amet. Curabitur tortor risus, tincidunt sed urna a, fermentum congue turpis nibh.</p>
</section>

<section class="slide quote-photo" style="left:324px;top:379px">
  <div class="photo" role="img" aria-label="Photo of an elderly man on a city bridge, with a purple tint" style="inset:0;background:linear-gradient(90deg,#9fb4c2 0%,#a7a3bd 35%,#a86cb4 70%,#8f3a9c 100%)"></div>
  <p class="abs quote" style="left:146px;top:48px;width:96px;color:#fff;font-size:6.2px">”Here you can write another inspirational quote or company goal”</p>
</section>

<section class="slide financials" style="left:611px;top:379px">
  <svg class="art" viewBox="0 0 267 150">
    <g stroke="#e3e3e3" stroke-width=".3">
      <line x1="48" y1="113" x2="146" y2="113"/><line x1="48" y1="106.2" x2="146" y2="106.2"/><line x1="48" y1="99.4" x2="146" y2="99.4"/><line x1="48" y1="92.6" x2="146" y2="92.6"/><line x1="48" y1="85.8" x2="146" y2="85.8"/><line x1="48" y1="79" x2="146" y2="79"/><line x1="48" y1="72.2" x2="146" y2="72.2"/><line x1="48" y1="65.4" x2="146" y2="65.4"/><line x1="48" y1="58.6" x2="146" y2="58.6"/><line x1="48" y1="51.8" x2="146" y2="51.8"/><line x1="48" y1="45" x2="146" y2="45"/>
    </g>
    <g font-size="2" fill="#555" font-family="Outfit, sans-serif" text-anchor="end">
      <text x="46" y="113.6">0%</text><text x="46" y="106.8">10%</text><text x="46" y="100">20%</text><text x="46" y="93.2">30%</text><text x="46" y="86.4">40%</text><text x="46" y="79.6">50%</text><text x="46" y="72.8">60%</text><text x="46" y="66">70%</text><text x="46" y="59.2">80%</text><text x="46" y="52.4">90%</text><text x="46" y="45.6">100%</text>
    </g>
    <g font-size="2" fill="#555" font-family="Outfit, sans-serif" text-anchor="middle">
      <text x="52" y="118">Jan</text><text x="60.3" y="118">Feb</text><text x="68.6" y="118">Mar</text><text x="76.9" y="118">Apr</text><text x="85.2" y="118">May</text><text x="93.5" y="118">Jun</text><text x="101.8" y="118">Jul</text><text x="110.1" y="118">Aug</text><text x="118.4" y="118">Sep</text><text x="126.7" y="118">Oct</text><text x="135" y="118">Nov</text><text x="143.3" y="118">Dec</text>
    </g>
    <polyline fill="none" stroke="#7a2d98" stroke-width=".6" points="52,94 60.3,87.2 68.6,85.8 76.9,80.4 85.2,68.8 93.5,68.8 101.8,60 110.1,55.2 118.4,54.5 126.7,55.2 135,51.8 143.3,55.2"/>
    <polyline fill="none" stroke="#2bb3e3" stroke-width=".6" points="52,109.6 60.3,106.2 68.6,102.8 76.9,98 85.2,92.6 93.5,94 101.8,98 110.1,91.2 118.4,82.4 126.7,72.2 135,68.8 143.3,75.6"/>
    <g fill="#7a2d98"><circle cx="52" cy="94" r=".8"/><circle cx="60.3" cy="87.2" r=".8"/><circle cx="68.6" cy="85.8" r=".8"/><circle cx="76.9" cy="80.4" r=".8"/><circle cx="85.2" cy="68.8" r=".8"/><circle cx="93.5" cy="68.8" r=".8"/><circle cx="101.8" cy="60" r=".8"/><circle cx="110.1" cy="55.2" r=".8"/><circle cx="118.4" cy="54.5" r=".8"/><circle cx="126.7" cy="55.2" r=".8"/><circle cx="135" cy="51.8" r=".8"/><circle cx="143.3" cy="55.2" r=".8"/></g>
    <g fill="#2bb3e3"><circle cx="52" cy="109.6" r=".8"/><circle cx="60.3" cy="106.2" r=".8"/><circle cx="68.6" cy="102.8" r=".8"/><circle cx="76.9" cy="98" r=".8"/><circle cx="85.2" cy="92.6" r=".8"/><circle cx="93.5" cy="94" r=".8"/><circle cx="101.8" cy="98" r=".8"/><circle cx="110.1" cy="91.2" r=".8"/><circle cx="118.4" cy="82.4" r=".8"/><circle cx="126.7" cy="72.2" r=".8"/><circle cx="135" cy="68.8" r=".8"/><circle cx="143.3" cy="75.6" r=".8"/></g>
    <g font-size="1.8" fill="#555" font-family="Outfit, sans-serif">
      <line x1="50" y1="110.8" x2="54" y2="110.8" stroke="#2bb3e3" stroke-width=".5"/><text x="55" y="111.4">Sales</text>
      <line x1="62" y1="110.8" x2="66" y2="110.8" stroke="#7a2d98" stroke-width=".5"/><text x="67" y="111.4">Revenue</text>
    </g>
  </svg>
  <h2 class="abs title" style="left:166px;top:40px">Financials</h2>
  <div class="rule" style="left:166px;top:55px"></div>
  <p class="abs body" style="left:166px;top:60px;width:62px">Mauris id interdum sapien, in convallis nulla. Integer laoreet nunc ut pharetra consequat. Cras sodales congue ante, eu blandit nulla hendrerit sed.</p>
</section>

<section class="slide competition" style="left:899px;top:379px">
  <h2 class="title-center" style="top:26px">Our competition</h2>
  <svg class="art" viewBox="0 0 267 150">
    <g fill="#fff" stroke="url(#line-grad)" stroke-width=".8">
      <rect x="-19" y="-19" width="38" height="38" rx="8" transform="translate(66 84) rotate(45)"/>
      <rect x="-19" y="-19" width="38" height="38" rx="8" transform="translate(133 84) rotate(45)"/>
      <rect x="-19" y="-19" width="38" height="38" rx="8" transform="translate(201 84) rotate(45)"/>
    </g>
  </svg>
  <div class="abs" style="left:47px;top:75px;width:38px;text-align:center"><p class="label">Competitor 1</p><p class="body" style="margin-top:2px">Mauris id interdum sapien, in convallis nulla.</p></div>
  <div class="abs" style="left:114px;top:75px;width:38px;text-align:center"><p class="label">Competitor 2</p><p class="body" style="margin-top:2px">Mauris id interdum sapien, in convallis nulla.</p></div>
  <div class="abs" style="left:182px;top:75px;width:38px;text-align:center"><p class="label">Competitor 3</p><p class="body" style="margin-top:2px">Mauris id interdum sapien, in convallis nulla.</p></div>
</section>

<!-- Row 4 -->
<section class="slide business" style="left:36px;top:550px">
  <svg class="art" viewBox="0 0 267 150">
    <polygon points="175,31 213,53 213,97 175,119 137,97 137,53" fill="none" stroke="url(#line-grad)" stroke-width=".6"/>
    <polygon transform="translate(175 75)" points="0,-26 22.5,-13 22.5,13 0,26 -22.5,13 -22.5,-13" fill="#fff" stroke="url(#line-grad)" stroke-width=".8" stroke-linejoin="round"/>
    <g stroke="url(#line-grad)" stroke-width=".7" stroke-linejoin="round">
      <polygon role="img" aria-label="Photo of city skyscrapers" transform="translate(175 31)" points="0,-13 11.3,-6.5 11.3,6.5 0,13 -11.3,6.5 -11.3,-6.5" fill="url(#photo-cool)"/>
      <polygon role="img" aria-label="Photo of a caregiver's hands" transform="translate(213 53)" points="0,-13 11.3,-6.5 11.3,6.5 0,13 -11.3,6.5 -11.3,-6.5" fill="url(#photo-warm)"/>
      <polygon role="img" aria-label="Photo of a phone screen with apps" transform="translate(213 97)" points="0,-13 11.3,-6.5 11.3,6.5 0,13 -11.3,6.5 -11.3,-6.5" fill="#2a3260"/>
      <polygon role="img" aria-label="Photo of a laboratory" transform="translate(175 119)" points="0,-13 11.3,-6.5 11.3,6.5 0,13 -11.3,6.5 -11.3,-6.5" fill="url(#photo-cool)"/>
      <polygon role="img" aria-label="Photo of paperwork and a pen" transform="translate(137 97)" points="0,-13 11.3,-6.5 11.3,6.5 0,13 -11.3,6.5 -11.3,-6.5" fill="#d9dbe6"/>
      <polygon role="img" aria-label="Photo of a woman meditating" transform="translate(137 53)" points="0,-13 11.3,-6.5 11.3,6.5 0,13 -11.3,6.5 -11.3,-6.5" fill="url(#photo-warm)"/>
    </g>
  </svg>
  <div class="wordmark" style="left:160px;top:70px;color:var(--purple)"><b style="font-size:6px">Corvath</b><span style="font-size:2.3px;letter-spacing:.3px">Therapeutics</span></div>
  <h2 class="abs title" style="left:40px;top:50px">Bussiness<br>Model</h2>
  <p class="abs body" style="left:40px;top:79px;width:62px">Mauris id interdum sapien, in convallis nulla. Integer laoreet nunc ut pharetra consequat. Cras sodales congue ante, eu blandit nulla hendrerit sed.</p>
</section>

<section class="slide mobile" style="left:324px;top:550px">
  <h2 class="title-center" style="top:24px">Mobile Application</h2>
  <p class="abs body" style="left:40px;top:49px;width:187px;text-align:center;color:#444">Lorem ipsum dolor sit amet, consectetur adipiscing elit. Morbi convallis mi leo, id pharetra urna scelerisque sit amet. Curabitur tortor risus, tincidunt sed urna a, fermentum congue turpis. Proin at viverra quam, id finibus odio.</p>
  <svg class="art" viewBox="0 0 267 150">
    <rect x="103" y="80" width="62" height="80" rx="8" fill="#fff" stroke="#c9c9c9" stroke-width=".6"/>
    <rect x="106" y="95" width="56" height="60" fill="#fff" stroke="#d5d5d5" stroke-width=".4"/>
    <circle cx="124.5" cy="87.5" r=".8" fill="#555"/>
    <circle cx="134" cy="84.5" r=".6" fill="#555"/>
    <line x1="130" y1="87.5" x2="138" y2="87.5" stroke="#555" stroke-width=".6" stroke-linecap="round"/>
  </svg>
  <div class="wordmark" style="left:119px;top:117px;color:var(--purple)"><b style="font-size:7px">Corvath</b><span style="font-size:2.6px;letter-spacing:.3px">Therapeutics</span></div>
</section>

<section class="slide questions" style="left:611px;top:550px">
  <svg class="art" viewBox="0 0 267 150">
    <polygon role="img" aria-label="Photo of a smiling woman" transform="translate(133 74)" points="0,-29 25.1,-14.5 25.1,14.5 0,29 -25.1,14.5 -25.1,-14.5" fill="url(#photo-warm)" stroke="url(#line-grad)" stroke-width=".9" stroke-linejoin="round"/>
    <circle cx="133" cy="74" r="11" fill="#fff"/>
    <g fill="none" stroke="#333" stroke-width=".5" stroke-linejoin="round">
      <path d="M128.5 72 a3.5 2.8 0 1 1 3 2.7 l-2 1.5 0.3-1.8 a3 3 0 0 1 -1.3-2.4z"/>
      <path d="M133.5 72.5 a3.3 2.6 0 1 1 3.3 3 l1.4 1.3 -2.3-.7"/>
    </g>
  </svg>
  <h2 class="abs title" style="left:50px;top:63px;font-size:10px">Questions</h2>
  <div class="rule" style="left:85px;top:77px"></div>
  <p class="abs body" style="left:168px;top:65px;width:58px">Mauris id interdum sapien, in convallis nulla. Integer laoreet nunc ut pharetra consequat. Cras sodales congue ante, eu blandit nulla hendrerit sed.</p>
</section>

<section class="slide closing" style="left:899px;top:550px">
  <div class="wordmark" style="left:117px;top:62px;color:var(--purple)">
    <b style="font-size:15px">Corvath</b>
    <span style="font-size:6.4px;margin-top:1px;color:var(--ink)">Therapeutics</span>
  </div>
</section>

<!-- Row 5 -->
<section class="slide client-notes" style="left:899px;top:729px">
  <h2 class="abs" style="left:40px;top:52px;font-size:7.4px;font-weight:500">For the client:</h2>
  <ol class="abs" style="left:40px;top:70px;width:170px;list-style:none;font-size:5.4px;line-height:1.2;color:var(--ink)">
    <li style="display:flex;gap:4px;margin-bottom:6px"><span>1.</span><span>All the photos, icons and graphics are free stock footage and can be changed, modified o replaced.</span></li>
    <li style="display:flex;gap:4px"><span>1.</span><span>I accept modifications in content, slides, distribution and style if clear brief and guidelines are provided.</span></li>
  </ol>
</section>

</body>
</html>
```